Australian Trucking Company Requires Professional Looking Stationary

We require a professional looking stationary design that incorporates our newly designed logo.

Our business, called "Vell Haulage Contracting", provides contracting work, transport and logistics to business in Western Australia particularly with links to the mining sector.

We are a small business looking to expand and our new logo and our new stationary will help develop our brand image in our market place.

Target Market(s)

Businesses and Corporation with links to the Mining Sector

Industry/Entity Type

Small Business

Requirements
Must have
• The letterhead must have the following details:
The new logo

Text saying: "Vell Haulage Pty Ltd (ACN 582 306 917) ATF The Vell Discretionary Trust T/AS"
"ABN 71 840 239 568"
Address "P.O Box 817 Ashbury WA, 6912"
Phone: 08 9172 5840
Email: vellhaul@mailnest.com.au

The text on the letterhead should be editable as the details are likely to change in the near future. Provision should be made for a website address all though one isn't available at the moment.

The styling, layout and font text is entirely up to the designer.

```html
<!DOCTYPE html>
<html lang="en">
<head>
<meta charset="utf-8">
<title>Vell Haulage Contracting – Letterhead</title>
<link href="https://fonts.googleapis.com/css2?family=PT+Sans+Narrow:wght@400;700&display=swap" rel="stylesheet">
<style>
  :root {
    --backdrop: #d6d6d6;
    --brand-red: #e30613;
    --brand-red-deep: #a10a12;
    --brand-red-soft: #ec4a52;
    --paper: #ffffff;
    --ink: #1a1a1a;
  }
  * { margin: 0; padding: 0; box-sizing: border-box; }
  html, body {
    width: 848px; height: 1200px; overflow: hidden;
    background: var(--backdrop);
  }
  .canvas { position: relative; width: 848px; height: 1200px; }
  .sheets { position: absolute; inset: 0; }
  .letterhead-header {
    position: absolute; top: 89px; left: 256px;
    font-family: "PT Sans Narrow", sans-serif;
    color: var(--ink);
  }
  .brand {
    position: absolute; left: 0; top: 2px; width: 160px;
    display: flex; align-items: flex-start; gap: 6px;
  }
  .brand-mark { width: 10px; height: 10px; background: var(--brand-red); margin-top: 3px; flex: none; }
  .brand-name {
    font-size: 13px; line-height: 12px; font-weight: 700;
    color: var(--brand-red); text-transform: uppercase;
  }
  .company-details, .registration-details {
    position: absolute; top: 0; white-space: nowrap;
    font-size: 9.5px; line-height: 11.5px;
  }
  .company-details { left: 178px; }
  .registration-details { left: 361px; }
  .detail-strong { font-weight: 700; }
  .letter-body {
    position: absolute; top: 234px; left: 310px; width: 392px;
    font-family: "PT Sans Narrow", sans-serif;
    font-size: 12.4px; line-height: 19.6px; color: var(--ink);
    text-align: left;
  }
</style>
</head>
<body>
<main class="canvas">
  <svg class="sheets" width="848" height="1200" viewBox="0 0 848 1200" aria-hidden="false">
    <defs>
      <linearGradient id="curl-shadow" x1="0" y1="0" x2="1" y2="0">
        <stop offset="0" stop-color="var(--brand-red-deep)" stop-opacity="0.75"/>
        <stop offset="0.35" stop-color="var(--brand-red-deep)" stop-opacity="0.55"/>
        <stop offset="1" stop-color="var(--brand-red-deep)" stop-opacity="0.35"/>
      </linearGradient>
      <linearGradient id="truck-fill" x1="0" y1="0" x2="1" y2="1">
        <stop offset="0" stop-color="var(--brand-red-soft)" stop-opacity="0.9"/>
        <stop offset="1" stop-color="var(--brand-red-soft)" stop-opacity="0.5"/>
      </linearGradient>
    </defs>
    <!-- reverse side of letterhead -->
    <rect class="reverse-sheet" x="56" y="297" width="596" height="841" fill="var(--brand-red)"/>
    <path class="reverse-illustration" role="img" aria-label="Large faint truck illustration across the lower left corner"
          d="M56 820 H330 C338 900 338 1020 335 1138 H56 Z" fill="url(#truck-fill)"/>
    <rect class="curl-shadow" x="204" y="297" width="448" height="592" fill="url(#curl-shadow)"/>
    <!-- front of letterhead with curled corner -->
    <path class="front-sheet" fill="var(--paper)"
          d="M204 47 H800 V887 C640 885 420 870 275 792 C240 620 216 360 204 47 Z"/>
  </svg>

  <header class="letterhead-header">
    <div class="brand">
      <span class="brand-mark"></span>
      <span class="brand-name">Vell Haulage<br>Contracting</span>
    </div>
    <address class="company-details" style="font-style:normal">
      <span class="detail-strong">Vell Haulage Pty Ltd</span><br>
      P.O Box 817 Ashbury WA, 6912<br>
      <span class="detail-strong">T :</span> 08 9172 5840&nbsp;&nbsp;<span class="detail-strong">E :</span> vellhaul@mailnest.com.au
    </address>
    <div class="registration-details">
      ABN 71 840 239 568<br>
      ACN 582 306 917<br>
      <span class="detail-strong">ATF</span> The Vell Discretionary Trust T/AS
    </div>
  </header>

  <p class="letter-body">Lorem ipsum dolor sit amet, consectetuer adipiscing elit. Aenean commodo ligula eget dolor. Aenean massa. Cum sociis natoque penatibus et magnis dis parturient montes, nascetur ridiculus mus. Donec quam felis, ultricies nec, pellentesque eu, pretium quis, sem. Nulla consequat massa quis enim. Donec pede justo, fringilla vel, aliquet nec, vulputate eget, arcu. In enim justo, rhoncus ut, imperdiet a, venenatis vitae, justo. Nullam dictum felis eu pede mollis pretium. Integer tincidunt. Cras dapibus. Vivamus elementum semper nisi. Aenean vulputate eleifend tellus. Aenean leo ligula, porttitor eu, consequat vitae, eleifend ac, enim. Aliquam lorem ante, dapibus in, viverra quis, feugiat a, tellus. Phasellus viverra nulla ut metus varius laoreet. Quisque rutrum. Aenean imperdiet. Etiam ultricies nisi vel augue. Curabitur ullamcorper ultricies nisi. Nam eget dui. Etiam rhoncus. Maecenas tempus, tellus eget condimentum rhoncus, sem quam semper libero, sit amet adipiscing sem neque sed ipsum. Nam quam nunc, blandit vel, luctus pulvinar, hendrerit id, lorem. Maecenas nec odio et ante tincidunt tempus. Donec vitae sapien ut libero venenatis faucibus. Nullam quis ante. Etiam sit amet orci eget eros faucibus tincidunt. Duis leo. Sed fringilla mauris sit amet nibh. Donec sodales sagittis magna. Sed consequat, leo eget bibendum sodales, augue velit cursus nunc</p>
</main>
</body>
</html>
```